Web Design Project

Create a web design

Target Market(s)

Upper class people interested in health

Requirements
Must have
• Templates
Nice to have
• Use the logo provided

```html
<!DOCTYPE html>
<html lang="en">
<head>
<meta charset="utf-8">
<title>Tidewell Health &amp; Fitness</title>
<link href="https://fonts.googleapis.com/css2?family=Open+Sans:wght@400;600;700&family=Reenie+Beanie&display=swap" rel="stylesheet">
<style>
  :root {
    --page-bg: #0b0b0b;
    --card: #ffffff;
    --green-top: #b9d63a;
    --green-bottom: #6f9a10;
    --green-text: #7a9a1a;
    --lime-link: #b5d334;
    --blue: #1a63a8;
    --blue-dark: #0c3f7c;
    --blue-light: #2f86d0;
    --band: #eeeed6;
    --grey-text: #666666;
    --grey-dark: #444444;
  }
  * { box-sizing: border-box; margin: 0; padding: 0; }
  html, body { width: 1200px; height: 565px; overflow: hidden; }
  body {
    position: relative;
    background: var(--page-bg);
    font-family: "Open Sans", Arial, sans-serif;
  }
  a { text-decoration: none; }
  .backdrop-photo {
    position: absolute; right: 0; top: 0; width: 460px; height: 565px;
    background: radial-gradient(ellipse at 65% 35%, #4a3f38 0%, #241e1a 40%, #0b0b0b 75%);
  }
  .site {
    position: absolute; left: 261px; top: 35px; width: 678px; height: 447px;
    background: var(--card); border-radius: 6px;
  }
  .main-nav {
    position: absolute; left: 7px; top: 7px; width: 664px; height: 35px;
    border-radius: 8px;
    background: linear-gradient(var(--green-top), var(--green-bottom));
  }
  .main-nav a {
    position: absolute; top: 9px;
    color: #fff; font-size: 12px; font-weight: 400; line-height: 16px;
    white-space: nowrap;
  }
  .main-nav a.active {
    top: 5px; padding: 4px 11px; border-radius: 6px;
    background: linear-gradient(var(--blue-light), var(--blue-dark));
  }
  .brand-band {
    position: absolute; left: 7px; top: 63px; width: 664px; height: 92px;
    border-radius: 6px;
    background: linear-gradient(90deg, var(--band) 0%, var(--band) 60%, #f7f7ec 100%);
  }
  .brand-name {
    position: absolute; left: 28px; top: 24px;
    font-size: 38px; font-weight: 600; color: var(--blue); line-height: 44px;
  }
  .trainer-photo {
    position: absolute; left: 394px; top: 50px; width: 260px; height: 395px;
    background: linear-gradient(180deg, #f3e6d2 0%, #f6efe8 50%, #ffffff 100%);
    border-radius: 120px 120px 0 0;
  }
  .tagline {
    position: absolute; left: 32px; top: 170px;
    font-family: "Reenie Beanie", cursive; font-size: 29px; line-height: 34px; color: var(--green-text);
  }
  .video-thumb {
    position: absolute; left: 21px; top: 218px; width: 141px; height: 92px;
    border-radius: 6px;
    background: linear-gradient(135deg, #8aa0c0, #c9b3c4 50%, #6d7f9c);
  }
  .video-thumb svg { position: absolute; left: 52px; top: 28px; }
  .promo { position: absolute; left: 176px; top: 221px; width: 270px; }
  .promo h2 { font-size: 13.5px; font-weight: 400; color: var(--blue); line-height: 15px; }
  .promo p { font-size: 8.5px; color: var(--grey-text); line-height: 12px; margin-top: 9px; }
  .promo .strong { font-size: 10px; font-weight: 600; color: var(--grey-dark); margin-top: 1px; }
  .promo h3 { font-size: 13px; font-weight: 400; color: #888; margin-top: 5px; line-height: 16px; }
  .promo .note { margin-top: 0; font-size: 8px; }
  .promo .note b { color: var(--grey-dark); }
  .cta {
    position: absolute; left: 176px; top: 341px; width: 125px; height: 27px;
    border-radius: 6px; border: 1px solid #6f9a10;
    background: linear-gradient(var(--green-top), var(--green-bottom));
    color: #fff; font-size: 10px; font-weight: 600;
    display: flex; align-items: center; justify-content: center;
  }
  .features { position: absolute; left: 7px; top: 383px; display: flex; gap: 15px; }
  .feature {
    position: relative; width: 155px; height: 56px; border-radius: 6px;
    border: 2px solid var(--blue-dark);
    background: linear-gradient(var(--blue-light), var(--blue) 55%, var(--blue-dark));
    color: #fff; font-size: 14px; line-height: 15px; padding: 11px 0 0 11px;
    overflow: hidden;
  }
  .feature .thumb {
    position: absolute; right: 0; top: 0; width: 62px; height: 52px;
    background: linear-gradient(90deg, rgba(255,255,255,0), #d9e3ee 60%, #b7c6d6);
  }
  .feature span { position: relative; }
  .footer {
    position: absolute; left: 0; top: 490px; width: 1200px; text-align: center;
    font-size: 8px; color: #cccccc;
  }
  .footer span { color: var(--lime-link); }
</style>
</head>
<body>
  <div class="backdrop-photo" role="img" aria-label="Close-up of a muscular torso in low light"></div>

  <main class="site">
    <nav class="main-nav">
      <a class="active" href="#" style="left:14px">Home</a>
      <a href="#" style="left:76px">Facilities</a>
      <a href="#" style="left:139px">Programs &amp; Services</a>
      <a href="#" style="left:263px">Membership</a>
      <a href="#" style="left:348px">Free Trials</a>
      <a href="#" style="left:420px">News &amp; Events</a>
      <a href="#" style="left:515px">Recruitment</a>
      <a href="#" style="left:598px">Contact</a>
    </nav>

    <header class="brand-band">
      <div class="brand-name">Tidewell</div>
    </header>

    <div class="trainer-photo" role="img" aria-label="Smiling trainer holding a water bottle and a green apple"></div>

    <p class="tagline">It's Crunch Time!</p>

    <div class="video-thumb" role="img" aria-label="Video still of a group fitness class stretching">
      <svg width="36" height="36" viewBox="0 0 36 36" aria-hidden="true">
        <rect width="36" height="36" rx="6" fill="rgba(0,0,0,0.45)"/>
        <path d="M14 10 L26 18 L14 26 Z" fill="#fff"/>
      </svg>
    </div>

    <section class="promo">
      <h2>12 weeks to change your body<br>for the rest of your life!</h2>
      <p>Watch this video to find out about my life-changing program. For less than the price of a cup of coffee per day, I can be your trainer.</p>
      <p class="strong">It can happen!</p>
      <h3>It's your time to shine!</h3>
      <p class="note">Presentation will be opening on <b>Monday 30th July, 2012</b></p>
    </section>

    <a class="cta" href="#">Sign up now to set up</a>

    <div class="features">
      <a class="feature" href="#"><i class="thumb" role="img" aria-label="Woman with toned abs"></i><span>Group fitness<br>Schedule</span></a>
      <a class="feature" href="#"><i class="thumb" role="img" aria-label="Woman lifting dumbbells"></i><span>Try us FREE<br>Today!</span></a>
      <a class="feature" href="#"><i class="thumb" role="img" aria-label="Two friends exercising"></i><span>Refer<br>a Friend</span></a>
      <a class="feature" href="#"><i class="thumb" role="img" aria-label="Woman holding a dumbbell"></i><span>Come &amp; Check<br>us Out!</span></a>
    </div>
  </main>

  <footer class="footer">Copyright 2012 © <span>Tidewell Personal Training</span></footer>
</body>
</html>
```